Namecard Designs+Logo for a High End Automobile Company

We need a new business card for our company called Velta Motorhof.

www.veltamotorhof.example.sg
Our new website will be up in 2.5 months time.

We sell used and brand new continental cars like Korvane, QTL, Dravell, Solbrini and etc. Currently we are operating from 2 offices in Singapore and United Kingdom.

We want a design which is serious. We are open to colours but try to keep it at a maximum of 3 colours.

We prefer something simple and minimal. We are open to 2 sides printing or even 2 sided namecards. Both UK and Singapore company offices address must be in; either side by side, front and back, or even 2 sided cards.

The logo can be a text logo, emblem, abstract, pictorial or combination.

We are printing with Pribo.com so please kindly follow the printing guideline.

http://uk.pribo.example/help/faq/templates-and-guidelines.html

Rich and Car Enthusiasts

Printing

Must have
• Our 2 offices; UK and Singapore.

Our slogan which is " The Automobile Specialist"
Should not have
• Not more than 3 colours

```html
<!DOCTYPE html>
<html lang="en">
<head>
<meta charset="utf-8">
<title>Velta Motorhof – Business Card</title>
<link rel="stylesheet" href="https://fonts.googleapis.com/css2?family=Arimo:wght@400&display=swap">
<style>
  :root {
    --backdrop: #545556;
    --card: #000000;
    --card-edge: #3d3e40;
    --brand-blue: #1e62a8;
    --pale-blue: #9ccbf2;
    --white: #ffffff;
    --muted: #4a4a4a;
    --font: "Arimo", Arial, sans-serif;
  }
  * { margin: 0; padding: 0; box-sizing: border-box; }
  html, body { width: 1200px; height: 933px; overflow: hidden; }
  body { background: var(--backdrop); font-family: var(--font); color: var(--white); position: relative; }

  .headline { position: absolute; left: 360px; top: 150px; width: 520px; text-align: right; }
  .headline__name { font-size: 53px; letter-spacing: 1px; line-height: 1; text-transform: uppercase; text-align: left; white-space: nowrap; }
  .headline__slogan { font-size: 26px; margin-top: 12px; letter-spacing: 0.5px; }

  .card { position: absolute; top: 355px; width: 546px; height: 333px; background: var(--card); border: 2px solid var(--card-edge); overflow: hidden; }
  .card--front { left: 38px; }
  .card--back { left: 618px; }

  .band { position: absolute; background: var(--brand-blue); }
  .card--front .band { left: 148px; top: 0; width: 244px; height: 58px; }
  .card--back .band { left: 146px; top: 0; width: 241px; height: 113px; }

  .wordmark { position: absolute; width: 260px; text-align: center; text-transform: uppercase; font-size: 26px; white-space: nowrap; }
  .wordmark__slogan { position: absolute; width: 260px; text-align: center; font-size: 10px; letter-spacing: 5px; white-space: nowrap; }
  .card--front .wordmark { left: 140px; top: 70px; color: var(--white); }
  .card--front .wordmark__slogan { left: 140px; top: 102px; color: var(--white); }
  .card--back .wordmark { left: 137px; top: 118px; color: var(--muted); }
  .card--back .wordmark__slogan { left: 137px; top: 150px; color: var(--muted); }

  .accent-rule { position: absolute; left: 146px; top: 168px; width: 241px; height: 5px; background: var(--brand-blue); }

  .feature-panel { position: absolute; left: 148px; top: 130px; width: 244px; height: 154px; background: var(--pale-blue); }

  .website { position: absolute; left: 0; top: 301px; width: 544px; text-align: center; font-size: 16px; }

  .person { position: absolute; left: 0; top: 200px; width: 544px; text-align: center; }
  .person__name { font-size: 17px; text-transform: uppercase; }
  .person__role { font-size: 13px; margin-top: 2px; }

  .contact { position: absolute; top: 256px; font-size: 12px; line-height: 15px; font-style: normal; white-space: nowrap; }
  .contact--address { right: 290px; text-align: right; }
  .contact--lines { left: 265px; }
</style>
</head>
<body>
  <header class="headline">
    <div class="headline__name">Velta Motorhof</div>
    <div class="headline__slogan">the automobile specialist</div>
  </header>

  <section class="card card--front" aria-label="Card front">
    <div class="band"></div>
    <div class="wordmark">Velta Motorhof</div>
    <div class="wordmark__slogan">the automobile specialist</div>
    <div class="feature-panel"></div>
    <div class="website">www.veltamotorhof.example.sg</div>
  </section>

  <section class="card card--back" aria-label="Card back">
    <div class="band"></div>
    <div class="wordmark">Velta Motorhof</div>
    <div class="wordmark__slogan">the automobile specialist</div>
    <div class="accent-rule"></div>
    <div class="person">
      <div class="person__name">Name Here</div>
      <div class="person__role">Job Name Here</div>
    </div>
    <address class="contact contact--address">
      UK · 14 Harlow Street<br>Brynmoor BR4 2QL<br>SG · 8 Kallang Rise<br>Singapore 339412
    </address>
    <div class="contact contact--lines">
      UK (0292) 555 000 000<br>SG +65 5550 0000<br>(0292) 555 000 000<br>mail@veltamotorhof.example
    </div>
  </section>
</body>
</html>
```